依頼詳細
イメージは以下の「もも雪ボンボン」のLPです。
https://www.marvinelle.jp/fs/marvinelle/gr52/mvlswh-014

こちらのLP同様、ファーストビューに「店頭POP画像」を必須で活用して下さい。

<ポイント>
・当店の客層は30~40代、ほとんどが女性です。
・多くの方が「ちょっとしたプレゼント、手土産」として購入されます。
人に渡したくなるような商品であることが伝わるようにお願いいたします。
・販売時期は6~8月を想定しています。夏季限定商品です。

記載していただきたい文章、店頭POP画像は添付ファイルをご確認下さい。
(本商品パッケージ写真、中身のゼリー形態写真は後ほど添付予定ですが、締め切りぎりぎりになってしまう可能性もありますので、仮の状態でご提案いただいても構いません。)

その他、なにか制作するうえで必要な情報などございましたら、いつでもご質問ください。
どうぞよろしくお願い申し上げます。
サイトURL
https://www.marvinelle.jp
ページ数
1ページ
希望イメージ
シンプル 複雑
単色 カラフル
暗い 明るい
日常 高級
遊び心 厳粛
未来的 伝統的
女性的 男性的
希望する色
ピンク×水色
納品ファイル
• 高解像度JPG (.jpg)
• イラストレーター形式 (.ai)
補足説明
店頭POPのリンク画像が含まれていないとのご指摘いただきました。
画像が重たく、添付できませんでしたので、以下よりダウンロードお願いいたします。
https://free.kitedrop.example/getbox_dlindex?rp=b81f03e6c4d297aa1e5c30f6b8d4e21k

また店頭POP画像を添付させていただきますので、ご確認お願い致します。
よろしくお願いいたします。
商品写真が間に合っておらず、大変申し訳ございません。

締め切りを延長させていただき、
写真素材が届きましたら、急いで添付させていただきます。

どうぞよろしくお願いいたします。
POPデータのダウンロード期限が切れてしまいましたので、更新いたしました。
以下よりお願い致します。

https://free.kitedrop.example/getbox_dlindex?rp=e47c1b5f8a03d926c4b1e7f02d5a93bk
商品画像の写真素材を3枚添付させていただきます。
遅くなってしまい、大変申し訳ございません。

ご提案、お待ちしております。
よろしくお願いいたします。
■ 選んだ理由

シンプルで分かりやすく、かつ夏らしい爽やかさも取り入れて下さっていて、
弊社のブランドイメージや商品の目指したい世界観とも合っているなと感じました。

■ 提案者全員のお礼・コメント

この度はたくさんのご提案いただきありがとうございました。
イメージに近いものが多く、とても迷ってしまいました。

また依頼を出させていただくこともあるかとも思いますので、
その際もぜひ、どうぞよろしくお願いいたします。

```html
<!DOCTYPE html>
<html lang="ja">
<head>
<meta charset="utf-8">
<title>完熟 白桃ゼリー</title>
<link rel="stylesheet" href="https://fonts.googleapis.com/css2?family=Noto+Sans+JP:wght@400;500;700;900&family=Zen+Maru+Gothic:wght@500;700;900&display=swap">
<style>
:root{
  --teal:#3f9a8e;
  --mint:#a6dcd4;
  --pink:#f4a7b9;
  --pink-soft:#fbd9e2;
  --pink-pale:#fdeef2;
  --red:#e2233b;
  --ink:#2b2b2b;
  --sky:#7cc7e6;
  --white:#ffffff;
}
*{margin:0;padding:0;box-sizing:border-box}
html,body{width:1200px;height:3604px;overflow:hidden;background:var(--white)}
body{font-family:"Noto Sans JP",sans-serif;color:var(--ink);position:relative}
.abs{position:absolute}

.season-bar{left:0;top:0;width:1200px;height:100px;background:var(--teal);display:flex;align-items:center;justify-content:center;color:var(--white);font-weight:700;font-size:42px;letter-spacing:6px;z-index:2}

.hero{left:0;top:100px;width:1200px;height:1500px;background:linear-gradient(180deg,#f7b8c7 0%,var(--pink) 60%,#f19bb0 100%);overflow:hidden}
.hero-band{left:-100px;top:560px;width:1400px;height:560px;background:var(--mint);transform:rotate(-6deg)}
.photo-peach-top{left:-60px;top:-40px;width:400px;height:340px;border-radius:50%;background:radial-gradient(circle at 55% 45%,#ffe7e0,#f59aa8 70%,#ec7e93)}
.tagline{left:0;top:70px;width:1200px;text-align:center;color:var(--white);font-weight:700;font-size:36px;font-style:italic;letter-spacing:2px}
.title{left:0;width:1200px;text-align:center;font-family:"Zen Maru Gothic",sans-serif;font-weight:900;color:var(--red);-webkit-text-stroke:14px var(--white);paint-order:stroke fill;line-height:1}
.title-ripe{top:170px;font-size:130px;letter-spacing:10px}
.title-name{top:320px;font-size:180px;letter-spacing:4px}
.photo-jelly{left:200px;top:720px;width:800px;height:500px;border-radius:50% 50% 46% 46%;background:radial-gradient(circle at 50% 40%,#fff5ef,#fcd6cf 55%,#f5b8b3)}
.photo-spoon{left:700px;top:520px;width:560px;height:180px;border-radius:90px 20px 20px 90px;background:linear-gradient(100deg,#f7f2ee,#d9d4d0);transform:rotate(-14deg)}
.spoon-note{left:740px;top:590px;font-weight:700;font-size:34px;color:var(--ink);transform:rotate(-22deg);letter-spacing:2px;white-space:nowrap}

.photo-box{left:40px;top:1000px;width:480px;height:380px;background:linear-gradient(160deg,#fbd3de,#f2a7bb);border-radius:8px}
.box-count{left:40px;top:1400px;font-size:26px;font-weight:500;color:var(--ink);white-space:nowrap}
.ripe-chip{left:600px;top:1110px;padding:6px 24px;background:var(--white);border-radius:20px;font-family:"Zen Maru Gothic",sans-serif;font-weight:900;font-size:100px;color:var(--red);line-height:1.1}
.name-small{left:600px;top:1262px;font-family:"Zen Maru Gothic",sans-serif;font-weight:900;font-size:110px;color:var(--red);-webkit-text-stroke:10px var(--white);paint-order:stroke fill;line-height:1;white-space:nowrap}
.origin-line{left:600px;top:1400px;font-size:40px;font-weight:700;color:var(--ink);letter-spacing:2px;white-space:nowrap}

.feature-head{display:flex;align-items:center;gap:14px;font-weight:900;font-size:44px;color:var(--ink);white-space:nowrap}
.feature-head svg{flex:none}
.feature-body{margin-top:40px;font-size:28px;line-height:1.8;color:#444;white-space:nowrap}

.pink-zone{left:0;top:2460px;width:1200px;height:700px}
.photo-peach{left:20px;top:1700px;width:520px;height:640px;border-radius:48%;background:radial-gradient(circle at 40% 40%,#ffe9e3,#f6a2ae 65%,#ee8497)}
.f1-text{left:600px;top:1750px;width:580px}
.f2-text{left:60px;top:2620px;width:540px}
.photo-jelly-bowl{left:600px;top:2540px;width:560px;height:440px;border-radius:50% 50% 44% 44%;background:radial-gradient(circle at 50% 40%,#fff6f0,#fbd5cd 60%,#f2b4af)}
.photo-gift{left:40px;top:3170px;width:540px;height:420px;border-radius:10px;background:linear-gradient(160deg,#fbd0db,#f3a8bc 60%,#fce4d6)}
.f3-text{left:600px;top:3200px;width:580px}
</style>
</head>
<body>

<header class="abs season-bar">夏季限定商品</header>

<section class="abs hero">
  <div class="abs hero-band"></div>
  <div class="abs photo-peach-top" role="img" aria-label="みずみずしい白桃の写真"></div>
  <p class="abs tagline">笑顔をみたいから、ちょっとした気配りに</p>
  <h1 class="abs title title-ripe">完熟</h1>
  <p class="abs title title-name">白桃ゼリー</p>
  <div class="abs photo-jelly" role="img" aria-label="ミントを添えた白桃ゼリーの写真"></div>
  <div class="abs photo-spoon" role="img" aria-label="白桃ゼリーをすくったスプーンの写真"></div>
  <p class="abs spoon-note">凍らせてもおいしい!</p>
  <div class="abs photo-box" role="img" aria-label="ピンクのギフトボックス商品写真"></div>
  <p class="abs box-count">3個入り（透明カップ65g/個）</p>
  <p class="abs ripe-chip">完熟</p>
  <p class="abs name-small">白桃ゼリー</p>
  <p class="abs origin-line">長野県産 川中島白桃使用</p>
</section>

<div class="abs photo-peach" role="img" aria-label="葉付きの白桃とカットした果肉の写真"></div>
<article class="abs f1-text">
  <h2 class="feature-head">
    <svg width="44" height="44" viewBox="0 0 44 44"><path d="M22 40C10 40 4 31 6 22 8 13 16 10 22 14 28 10 36 13 38 22 40 31 34 40 22 40Z" fill="var(--sky)"/><path d="M22 14C22 9 25 5 30 4 29 9 26 12 22 14Z" fill="var(--sky)"/></svg>
    長野県産 川中島白桃使用
  </h2>
  <p class="feature-body">果肉が大きくジューシーで、<br>コクのある甘みが特徴の川中島白桃。<br>桃の甘みと香りがぎゅっと詰まった<br>ゼリーです。</p>
</article>

<svg class="abs pink-zone" viewBox="0 0 1200 700" preserveAspectRatio="none"><path d="M0 0 L600 60 L1200 0 L1200 640 L600 700 L0 640Z" fill="var(--pink-soft)"/></svg>

<article class="abs f2-text">
  <h2 class="feature-head">
    <svg width="44" height="44" viewBox="0 0 44 44"><path d="M22 40C10 40 4 31 6 22 8 13 16 10 22 14 28 10 36 13 38 22 40 31 34 40 22 40Z" fill="var(--sky)"/><path d="M22 14C22 9 25 5 30 4 29 9 26 12 22 14Z" fill="var(--sky)"/></svg>
    凍らせてもおいしい!
  </h2>
  <p class="feature-body">凍らせると、まるで白桃そのものを<br>食べているようなとろっとした食感を<br>お楽しみいただけます。</p>
</article>
<div class="abs photo-jelly-bowl" role="img" aria-label="器に盛った白桃ゼリーの写真"></div>

<div class="abs photo-gift" role="img" aria-label="ピンクの箱とカップ型ゼリー3個の商品写真"></div>
<article class="abs f3-text">
  <h2 class="feature-head">
    <svg width="44" height="44" viewBox="0 0 44 44"><path d="M22 40C10 40 4 31 6 22 8 13 16 10 22 14 28 10 36 13 38 22 40 31 34 40 22 40Z" fill="var(--sky)"/><path d="M22 14C22 9 25 5 30 4 29 9 26 12 22 14Z" fill="var(--sky)"/></svg>
    プレゼントにもぴったり!
  </h2>
  <p class="feature-body">可愛らしいピンク色のボックスなので、<br>プレゼントや手土産にもぴったりです。<br>（カップ型ゼリー・3個入り）</p>
</article>

</body>
</html>
```